Brand Business Card for Hotel Cloud Management System

Hello designers,
we are looking for a new brand business card for our product Stayvora. Our brand Stayvora is a hotel management system for small hotels, B&B, guesthouses etc. and just recently we are expanding our offer to other European markets. Therefore we need a business card that will communicate not only to the end-users (hoteliers) but also to potential business partners/ We would like the brand business card to be professional looking, but not too serius, modern, elegant, clean, Our brand color is orange, dark grey and it would be nice to see both combined.

Please visit our website www.stayvora.eu to get more impression on what our brand stayvora stands for.

Please find attached stayvora logo.

Target Market(s)

small hotels, hoteliers, B&B owners, potential business partners

Industry/Entity Type

Software Service

Contact Information for Business Card

Stayvora
- hotel software solutions - web booking engine - multi channel manager
www.stayvora.eu
T: +38614738265
E: info@stayvora.net

Font styles to use
Serif
Sans Serif

Colors
f37122
aaaaaa
606060
f6f6f6

Requirements
Must have
• Logo of the brand
• the layout of the business card should be in connection with the look and feel of the website stayvora.eu and logo stayvora;

```html
<!DOCTYPE html>
<html lang="en">
<head>
<meta charset="utf-8">
<title>Stayvora Business Card</title>
<link rel="stylesheet" href="https://fonts.googleapis.com/css2?family=Arimo:wght@400;700&display=swap">
<style>
  :root {
    --brand-orange: #f37122;
    --brand-orange-deep: #d8661c;
    --charcoal: #2a2a2a;
    --charcoal-dark: #1f1f1f;
    --ink: #333333;
    --mid-grey: #606060;
    --soft-grey: #aaaaaa;
    --paper: #f6f6f6;
    --white: #ffffff;
    --stage: #e9e9e9;
  }
  * { box-sizing: border-box; margin: 0; padding: 0; }
  html, body {
    width: 1200px; height: 997px; overflow: hidden;
    background: var(--stage);
    font-family: "Arimo", Arial, sans-serif;
  }
  .business-card {
    position: absolute; left: 180px; top: 258px;
    width: 840px; height: 480px;
    border-radius: 28px; overflow: hidden;
    box-shadow: 0 12px 30px rgba(0,0,0,0.25);
    display: flex; flex-direction: column;
  }
  .card-header {
    height: 210px;
    background: linear-gradient(180deg, var(--white) 0%, var(--paper) 70%, #e4e4e4 100%);
    display: flex; flex-direction: column; align-items: center; justify-content: center;
  }
  .brand-lockup { display: flex; align-items: center; gap: 14px; }
  .brand-square { width: 30px; height: 30px; background: var(--brand-orange); border-radius: 4px; }
  .brand-name {
    font-size: 64px; font-weight: 700; color: var(--charcoal);
    letter-spacing: -1px; line-height: 1;
  }
  .brand-tagline {
    margin-top: 6px; font-size: 22px; color: var(--mid-grey); letter-spacing: 0.5px;
  }
  .card-body {
    flex: 1;
    background: linear-gradient(180deg, var(--charcoal) 0%, var(--charcoal-dark) 100%);
    position: relative;
    display: flex; align-items: center;
  }
  .holder {
    position: absolute; left: 70px; bottom: 42px;
  }
  .holder-name {
    font-size: 26px; font-weight: 700; color: var(--brand-orange); letter-spacing: 0.5px;
  }
  .holder-role { font-size: 22px; color: #e2e2e2; margin-top: 4px; }
  .divider {
    position: absolute; left: 400px; top: 30px; width: 2px; height: 150px;
    background: linear-gradient(180deg, transparent, var(--brand-orange) 50%, transparent);
  }
  .contact-list {
    position: absolute; left: 470px; top: 40px; list-style: none;
    display: flex; flex-direction: column; gap: 18px;
  }
  .contact-item { display: flex; align-items: center; gap: 18px; color: #e8e8e8; font-size: 21px; }
  .contact-item.web { font-weight: 700; }
  .contact-icon {
    width: 30px; height: 30px; border-radius: 50%;
    background: var(--paper); display: flex; align-items: center; justify-content: center;
  }
  .card-footer {
    height: 60px;
    background: linear-gradient(180deg, var(--brand-orange) 0%, var(--brand-orange-deep) 100%);
    display: flex; align-items: center; padding-left: 70px;
    font-size: 19px; color: var(--charcoal); letter-spacing: 0.6px; text-transform: uppercase;
  }
  .service-sep { margin: 0 8px; color: var(--white); }
</style>
</head>
<body>
  <section class="business-card">
    <header class="card-header">
      <div class="brand-lockup">
        <span class="brand-square"></span>
        <span class="brand-name">Stayvora</span>
      </div>
      <div class="brand-tagline">hotel pms service</div>
    </header>

    <div class="card-body">
      <div class="holder">
        <div class="holder-name">MAREK DOLAN</div>
        <div class="holder-role">Managing Director</div>
      </div>
      <div class="divider"></div>
      <ul class="contact-list">
        <li class="contact-item">
          <span class="contact-icon">
            <svg width="16" height="16" viewBox="0 0 24 24"><path fill="#f37122" d="M6.6 10.8a15 15 0 0 0 6.6 6.6l2.2-2.2a1 1 0 0 1 1-.25 11.4 11.4 0 0 0 3.6.57 1 1 0 0 1 1 1V20a1 1 0 0 1-1 1A17 17 0 0 1 3 4a1 1 0 0 1 1-1h3.5a1 1 0 0 1 1 1c0 1.25.2 2.45.57 3.57a1 1 0 0 1-.25 1z"/></svg>
          </span>
          +38614738265
        </li>
        <li class="contact-item">
          <span class="contact-icon">
            <svg width="16" height="16" viewBox="0 0 24 24"><path fill="#f37122" d="M3 5h18a1 1 0 0 1 1 1v12a1 1 0 0 1-1 1H3a1 1 0 0 1-1-1V6a1 1 0 0 1 1-1zm9 7.5L20 7H4z"/></svg>
          </span>
          info@stayvora.net
        </li>
        <li class="contact-item web">
          <span class="contact-icon">
            <svg width="16" height="16" viewBox="0 0 24 24"><path fill="#f37122" d="M12 2a7 7 0 0 1 7 7c0 5-7 13-7 13S5 14 5 9a7 7 0 0 1 7-7zm0 4.5A2.5 2.5 0 1 0 12 11.5 2.5 2.5 0 0 0 12 6.5z"/></svg>
          </span>
          www.stayvora.eu
        </li>
      </ul>
    </div>

    <footer class="card-footer">
      Hotel software solutions<span class="service-sep">•</span>Web booking engine<span class="service-sep">•</span>Multi channel manager
    </footer>
  </section>
</body>
</html>
```